Dutch psychology podcast needs logo / art design

I need a logo / artwork for my new podcast on psychology/health called 'Het Heldere Kwartier'. In the podcast I talk to different experts on subjects as personal development, psychology, health, spirituality and entrepreneurship. I would like to see my brand colors back in the design (www.joramveldkuijl.nl) and my face in the artwork since I'm the host of the show.

My photo is included in the attachments and I've also added some examples of what I'm looking for.

Industry/Entity Type

Psychology

Colors

Designer to choose colors to be used in the design.

Requirements
Must have
• - Name of the show: 'Het Heldere Kwartier' (I prefer that this name is turned into a logo), see attachment of example of Harbor of Wonder
• - Subtitle: 'met Joram Veldkuijl' which is my name a the host
• - My picture, see attachments

```html
<!DOCTYPE html>
<html lang="nl">
<head>
<meta charset="utf-8">
<title>Het Heldere Kwartier</title>
<link href="https://fonts.googleapis.com/css2?family=Bowlby+One+SC&family=Rubik:wght@800&display=swap" rel="stylesheet">
<style>
  :root {
    --teal-deep: #189e98;
    --teal-mid: #45b2ae;
    --teal-light: #c3e6e4;
    --pill: #3bae95;
    --white: #ffffff;
    --navy: #1b2238;
    --skin: #d9a48c;
  }
  html, body {
    margin: 0;
    padding: 0;
    overflow: hidden;
    width: 1200px;
    height: 1200px;
  }
  .cover {
    position: relative;
    width: 1200px;
    height: 1200px;
    overflow: hidden;
    background: linear-gradient(90deg, var(--teal-deep) 0%, var(--teal-deep) 35%, var(--teal-mid) 62%, var(--teal-light) 100%);
  }
  .show-title {
    position: absolute;
    left: 58px;
    top: 190px;
    margin: 0;
    font-family: "Bowlby One SC", "Arial Black", sans-serif;
    font-weight: 400;
    font-size: 150px;
    line-height: 0.98;
    color: var(--white);
    text-transform: uppercase;
    transform: skewY(-14deg);
    transform-origin: left top;
    letter-spacing: -2px;
    white-space: nowrap;
  }
  .show-title span { display: block; }
  .host-photo {
    position: absolute;
    left: 0;
    top: 0;
    width: 1200px;
    height: 1200px;
  }
  .host-badge {
    position: absolute;
    left: 276px;
    top: 817px;
    width: 586px;
    height: 108px;
    border-radius: 36px;
    background: var(--pill);
    box-shadow: 0 6px 18px rgba(0, 0, 0, 0.12);
    display: flex;
    align-items: center;
    justify-content: center;
    font-family: "Rubik", sans-serif;
    font-weight: 800;
    font-size: 31px;
    letter-spacing: 0.5px;
    color: var(--white);
    text-transform: uppercase;
  }
  .sound-wave {
    position: absolute;
    left: 446px;
    top: 924px;
    width: 250px;
    height: 190px;
  }
</style>
</head>
<body>
<main class="cover">
  <h1 class="show-title">
    <span>Het</span>
    <span>Heldere</span>
    <span>Kwartier</span>
  </h1>

  <svg class="host-photo" viewBox="0 0 1200 1200" role="img" aria-label="Portretfoto van host Joram Veldkuijl, glimlachend met gekruiste armen, in een donkerblauwe trui">
    <defs>
      <linearGradient id="skinTone" x1="0" y1="0" x2="0" y2="1">
        <stop offset="0" stop-color="#2b2a2c"/>
        <stop offset="0.22" stop-color="#c99580"/>
        <stop offset="1" stop-color="#b98571"/>
      </linearGradient>
    </defs>
    <rect x="705" y="238" width="290" height="470" rx="140" fill="url(#skinTone)"/>
    <rect x="482" y="690" width="718" height="510" rx="90" fill="var(--navy)"/>
  </svg>

  <div class="host-badge">met Joram Veldkuijl</div>

  <svg class="sound-wave" viewBox="0 0 250 190" aria-hidden="true">
    <g fill="var(--white)">
      <rect x="6" y="70" width="12" height="50" rx="6"/>
      <rect x="31" y="42" width="12" height="106" rx="6"/>
      <rect x="56" y="2" width="12" height="186" rx="6"/>
      <rect x="80" y="42" width="12" height="106" rx="6"/>
      <rect x="105" y="70" width="12" height="50" rx="6"/>
      <rect x="129" y="70" width="12" height="50" rx="6"/>
      <rect x="153" y="42" width="12" height="106" rx="6"/>
      <rect x="178" y="2" width="12" height="186" rx="6"/>
      <rect x="203" y="42" width="12" height="106" rx="6"/>
      <rect x="228" y="70" width="12" height="50" rx="6"/>
    </g>
  </svg>
</main>
</body>
</html>
```